Van Wrap Design Painting Contractor Company

We need eye catching wrap design for painting contractor company
Has to be useable on our two van;; Vortane Halden production year 2001 ( white colour) , and Vortane Pilcaro Duna production year 2019 ( gray colour )
Sides and back of vans has to be similar

***Wrap design to include both sides, front hood and rear doors !!!!
***** since like our Company name is Kolvan+ Nudo wich mean that we act fast, the wrap design has to be in that way ( fast, trusted, strong)

I prefer red, green and blue colour, but I’m open for colour suggestions.
Has to be eye catching, memorable, noticeable and cool looking!!!!

Target Market(s)

Private and Commercial

Requirements
Must have
• 1. Logo, company name, phone number
2. Main Service description : SOBOSLIKAR
3. Secondary service description: Završni Radovi u Interijeru
4. website: KolvanNudo.net or just #KolvanNudo
Nice to have
• Icon:
1.Gremlot, Tavoline,
2.paintbrush, spray gunn on rear door
3. Company name on front bonnet
4. painter silhouette on ladder
Should not have
• ?

```html
<!DOCTYPE html>
<html lang="hr">
<head>
<meta charset="utf-8">
<title>KolvanNudo – Van Wrap</title>
<link rel="stylesheet" href="https://fonts.googleapis.com/css2?family=Ubuntu:wght@500;700&family=Arimo:wght@400&display=swap">
<style>
  :root{
    --bg:#121212;
    --lime:#a6d63a;
    --lime-bright:#c4ef4a;
    --green:#27a23b;
    --yellow:#f2e531;
    --blue:#2a5caa;
    --white:#f4f4f2;
    --slate:#3f4a5a;
    --dark:#232426;
    --glass:#2b2f33;
    --tire:#1a1a1a;
    --rim:#b8bcc0;
  }
  html,body{margin:0;padding:0;overflow:hidden;background:var(--bg);}
  .canvas{width:819px;height:1200px;display:block;}
  .brand{font-family:"Ubuntu",sans-serif;font-weight:500;}
  .tagline{font-family:"Arimo",sans-serif;font-weight:400;}
  .contact{font-family:"Ubuntu",sans-serif;font-weight:700;}
  .service{font-family:"Ubuntu",sans-serif;font-weight:700;}
  .subservice{font-family:"Ubuntu",sans-serif;font-weight:500;}
  .social{font-family:"Ubuntu",sans-serif;font-weight:500;}
</style>
</head>
<body>
<svg class="canvas" viewBox="0 0 819 1200" xmlns="http://www.w3.org/2000/svg">
  <defs>
    <linearGradient id="grey-wrap" x1="0" y1="0" x2="1" y2="0.3">
      <stop offset="0" stop-color="#4a5668"/>
      <stop offset="0.45" stop-color="#7f9a58"/>
      <stop offset="1" stop-color="#9cc64a"/>
    </linearGradient>
    <linearGradient id="grey-skirt" x1="0" y1="0" x2="1" y2="0">
      <stop offset="0" stop-color="#2f3844"/>
      <stop offset="0.6" stop-color="#3d4a4c"/>
      <stop offset="1" stop-color="#5a7040"/>
    </linearGradient>
    <linearGradient id="white-wave" x1="0" y1="0" x2="1" y2="0">
      <stop offset="0" stop-color="#e9ea88"/>
      <stop offset="0.5" stop-color="#b9e0a0"/>
      <stop offset="1" stop-color="#e6ef7a"/>
    </linearGradient>
    <linearGradient id="hood-wrap" x1="0" y1="0" x2="1" y2="1">
      <stop offset="0" stop-color="#bfe6b8"/>
      <stop offset="0.5" stop-color="#9fd8cf"/>
      <stop offset="1" stop-color="#d5ea8e"/>
    </linearGradient>
    <g id="phone-icon">
      <path d="M1 2 Q1 0 3 0 L4 0 L5 3 L3.5 4 Q5 7 8 8.5 L9 7 L12 8 L12 9 Q12 11 10 11 Q1 10 1 2Z"/>
    </g>
    <g id="globe-icon" fill="none" stroke-width="1.2">
      <circle cx="6" cy="6" r="5.5"/>
      <ellipse cx="6" cy="6" rx="2.4" ry="5.5"/>
      <line x1="0.5" y1="6" x2="11.5" y2="6"/>
      <line x1="1.5" y1="3" x2="10.5" y2="3"/>
      <line x1="1.5" y1="9" x2="10.5" y2="9"/>
    </g>
    <g id="wheel-compact">
      <circle r="42" fill="var(--tire)"/>
      <circle r="28" fill="var(--rim)"/>
      <circle r="9" fill="#8d9196"/>
    </g>
    <g id="wheel-panel">
      <circle r="45" fill="var(--tire)"/>
      <circle r="28" fill="#9ea2a6"/>
      <circle r="20" fill="none" stroke="#7d8186" stroke-width="2"/>
      <circle r="7" fill="#6d7176"/>
    </g>
  </defs>

  <!-- Compact van, left side -->
  <g class="van compact-side">
    <g class="roof-rails" fill="var(--dark)">
      <rect x="128" y="106" width="250" height="4" rx="2"/>
      <rect x="128" y="103" width="10" height="10" rx="2"/>
      <rect x="262" y="102" width="14" height="11" rx="2"/>
      <rect x="385" y="99" width="12" height="14" rx="2"/>
    </g>
    <path class="body" d="M100 332 L95 165 Q96 124 128 118 L470 112 Q505 113 525 132 L588 196 Q660 212 700 242 Q720 258 719 300 L716 330 Q712 342 700 342 L668 342 A52 52 0 0 0 564 342 L228 342 A52 52 0 0 0 122 342 Z" fill="url(#grey-wrap)"/>
    <path class="skirt" d="M100 282 L700 292 Q716 300 717 320 L716 330 Q712 342 700 342 L668 342 A52 52 0 0 0 564 342 L228 342 A52 52 0 0 0 122 342 L100 332 Z" fill="url(#grey-skirt)" opacity="0.9"/>
    <path class="wave" d="M100 160 Q250 135 380 165 Q470 185 560 175 L560 200 Q460 210 370 190 Q240 165 100 190 Z" fill="var(--yellow)" opacity="0.18"/>
    <path class="window" d="M280 140 L378 138 Q384 140 384 148 L384 218 Q382 222 376 222 L284 222 Q280 220 280 214 Z" fill="var(--glass)"/>
    <path class="window" d="M408 142 Q408 138 414 138 L475 138 Q488 140 498 152 L548 216 Q548 224 540 224 L414 224 Q408 222 408 216 Z" fill="var(--glass)"/>
    <g class="door-lines" stroke="#2c3440" stroke-width="1.2" fill="none" opacity="0.7">
      <path d="M265 125 L268 334"/>
      <path d="M395 120 L398 336"/>
      <path d="M560 205 L562 300"/>
    </g>
    <rect class="handle" x="150" y="220" width="110" height="7" rx="3" fill="var(--dark)" opacity="0.85"/>
    <rect class="handle" x="296" y="283" width="244" height="6" rx="3" fill="var(--dark)" opacity="0.6"/>
    <path class="mirror" d="M515 190 Q540 186 548 198 L546 214 L518 212 Z" fill="var(--dark)"/>
    <path class="headlight" d="M668 225 Q700 230 708 250 L686 250 Q672 242 668 225 Z" fill="#d7dde2"/>
    <path class="bumper" d="M690 262 Q718 268 719 300 L716 330 Q712 342 700 342 L672 342 Q670 300 690 262 Z" fill="var(--dark)"/>
    <rect class="tail-light" x="92" y="175" width="6" height="45" rx="2" fill="#a02a2a"/>
    <path class="band" d="M100 248 L700 258 L690 282 L100 270 Z" fill="var(--lime)"/>
    <use href="#wheel-compact" x="175" y="330"/>
    <use href="#wheel-compact" x="616" y="330"/>
    <circle class="logo-dot" cx="188" cy="160" r="34" fill="var(--lime)"/>
    <text class="brand" x="104" y="212" font-size="21" fill="var(--yellow)">KolvanNudo</text>
    <text class="tagline" x="112" y="242" font-size="14" fill="var(--yellow)">Professional Services</text>
    <use href="#phone-icon" x="244" y="258" fill="var(--blue)"/>
    <text class="contact" x="260" y="270" font-size="13" fill="var(--blue)">+385 91 000 4821</text>
    <use href="#globe-icon" x="408" y="262" stroke="var(--blue)"/>
    <text class="contact" x="430" y="274" font-size="13" fill="var(--blue)" letter-spacing="0.5">KOLVANNUDO.NET</text>
    <text class="service" x="278" y="314" font-size="15" fill="var(--lime-bright)">SOBOSLIKAR</text>
    <text class="subservice" x="384" y="315" font-size="12.5" fill="var(--yellow)">Završni Radovi u Interijeru</text>
    <text class="social" x="604" y="240" font-size="7" fill="var(--yellow)">Gremlot · Tavoline</text>
  </g>

  <!-- Panel van, right side -->
  <g class="van panel-side">
    <g class="roof-rails" fill="var(--dark)">
      <rect x="170" y="462" width="240" height="4" rx="2"/>
      <rect x="172" y="454" width="6" height="14"/>
      <rect x="268" y="454" width="6" height="14"/>
      <rect x="400" y="454" width="6" height="14"/>
    </g>
    <path class="body" d="M90 722 L88 500 Q90 472 120 470 L545 468 Q566 470 580 490 L640 585 Q708 612 728 640 Q736 662 734 700 L730 722 L690 722 A52 52 0 0 0 586 722 L252 722 A52 52 0 0 0 148 722 Z" fill="var(--white)"/>
    <path class="wave" d="M88 520 Q300 480 470 510 L470 560 Q300 530 88 570 Z" fill="url(#white-wave)" opacity="0.75"/>
    <path class="wave" d="M88 615 Q350 580 520 630 Q640 660 735 640 L735 670 Q600 690 450 655 Q300 620 88 660 Z" fill="url(#white-wave)" opacity="0.7"/>
    <path class="window" d="M478 498 Q478 490 486 490 L550 490 Q568 494 580 512 L625 582 Q624 590 616 590 L486 590 Q478 588 478 580 Z" fill="#3a3a3a"/>
    <path class="mirror" d="M602 552 Q620 550 624 562 L622 594 L606 594 Z" fill="var(--dark)"/>
    <path class="band" d="M88 574 L620 578 Q680 590 705 612 L88 610 Z" fill="var(--blue)"/>
    <g class="door-lines" stroke="#c4c6c4" stroke-width="1.2" fill="none">
      <path d="M280 472 L280 718"/>
      <path d="M460 472 L462 718"/>
      <path d="M476 598 L476 718"/>
    </g>
    <rect class="handle" x="118" y="613" width="170" height="9" rx="4" fill="var(--dark)"/>
    <rect class="handle" x="424" y="610" width="36" height="14" rx="3" fill="var(--dark)"/>
    <rect class="handle" x="462" y="610" width="22" height="14" rx="3" fill="var(--dark)"/>
    <path class="trim" d="M252 690 L586 692 L586 700 L252 698 Z" fill="var(--dark)"/>
    <path class="trim" d="M82 672 L148 672 Q150 700 150 722 L84 722 Q80 700 82 672 Z" fill="var(--dark)"/>
    <path class="bumper" d="M690 700 L730 688 Q738 700 734 712 L730 722 L690 722 Z" fill="var(--dark)"/>
    <rect class="tail-light" x="86" y="600" width="8" height="58" rx="2" fill="#a02a2a"/>
    <path class="headlight" d="M712 642 Q730 644 732 666 L716 666 Z" fill="#e0b070"/>
    <use href="#wheel-panel" x="200" y="730"/>
    <use href="#wheel-panel" x="638" y="730"/>
    <circle class="logo-dot" cx="155" cy="524" r="42" fill="var(--blue)"/>
    <text class="brand" x="206" y="540" font-size="30" fill="var(--blue)">KolvanNudo</text>
    <text class="tagline" x="240" y="565" font-size="18" fill="var(--blue)">Professional Services</text>
    <use href="#phone-icon" x="118" y="584" fill="var(--yellow)"/>
    <text class="contact" x="134" y="597" font-size="14" fill="var(--yellow)">+385 91 000 4821</text>
    <use href="#globe-icon" x="275" y="586" stroke="var(--yellow)"/>
    <text class="contact" x="297" y="598" font-size="14" fill="var(--yellow)" letter-spacing="0.6">KOLVANNUDO.NET</text>
    <text class="service" x="118" y="646" font-size="22" fill="var(--blue)">SOBOSLIKAR</text>
    <text class="subservice" x="262" y="646" font-size="16" fill="var(--green)">Završni Radovi u Interijeru</text>
    <text class="social" x="410" y="494" font-size="8" fill="var(--blue)">Gremlot · Tavoline</text>
    <rect class="partner-badge" x="497" y="627" width="80" height="14" rx="2" fill="#d6d8d4"/>
  </g>

  <!-- Rear doors -->
  <g class="van rear-doors">
    <path class="body" d="M86 1100 L84 848 Q86 814 120 812 L340 812 Q372 814 374 848 L378 1100 Z" fill="var(--white)"/>
    <path class="wave" d="M160 870 Q260 900 375 870 L375 1000 Q300 960 190 990 Z" fill="url(#white-wave)" opacity="0.7"/>
    <line x1="230" y1="812" x2="232" y2="1100" stroke="#c8c8c8" stroke-width="1"/>
    <rect class="hinge" x="76" y="888" width="22" height="16" rx="4" fill="var(--white)" stroke="var(--dark)" stroke-width="2"/>
    <rect class="hinge" x="356" y="888" width="22" height="16" rx="4" fill="var(--white)" stroke="var(--dark)" stroke-width="2"/>
    <rect class="tail-light" x="84" y="975" width="18" height="62" rx="4" fill="#8e2424"/>
    <rect class="tail-light" x="358" y="975" width="18" height="62" rx="4" fill="#8e2424"/>
    <rect class="handle" x="114" y="980" width="108" height="14" rx="5" fill="var(--dark)"/>
    <rect class="handle" x="234" y="975" width="26" height="18" rx="3" fill="var(--dark)"/>
    <rect class="plate" x="126" y="998" width="84" height="20" rx="2" fill="#eceeee" stroke="#555" stroke-width="1"/>
    <rect class="bumper" x="82" y="1050" width="300" height="44" rx="6" fill="var(--dark)"/>
    <rect class="bumper-edge" x="94" y="1094" width="276" height="10" rx="3" fill="#3a3b3d"/>
    <rect class="painter-silhouette" x="98" y="848" width="52" height="200" fill="var(--green)" opacity="0.85" role="img" aria-label="Painter silhouette on a ladder with spray gun"/>
    <circle class="logo-dot" cx="228" cy="856" r="30" fill="var(--blue)"/>
    <text class="social" x="300" y="872" font-size="8" fill="var(--blue)">Gremlot · Tavoline</text>
    <text class="brand" x="138" y="920" font-size="22" fill="var(--blue)">KolvanNudo</text>
    <text class="tagline" x="162" y="941" font-size="13" fill="var(--blue)">Professional Services</text>
    <rect class="band" x="84" y="948" width="292" height="22" fill="var(--blue)"/>
    <use href="#phone-icon" x="95" y="953" fill="var(--yellow)"/>
    <text class="contact" x="110" y="964" font-size="11" fill="var(--yellow)">+385 91 000 4821</text>
    <use href="#globe-icon" x="220" y="953" stroke="var(--yellow)"/>
    <text class="contact" x="240" y="964" font-size="11" fill="var(--yellow)" letter-spacing="0.4">KOLVANNUDO.NET</text>
    <text class="service" x="224" y="1022" font-size="18" fill="var(--blue)">SOBOSLIKAR</text>
    <text class="subservice" x="164" y="1042" font-size="13.5" fill="var(--green)">Završni Radovi u Interijeru</text>
  </g>

  <!-- Front hood -->
  <g class="van front-hood">
    <path class="body" d="M448 1110 L444 900 Q446 835 488 818 Q520 810 593 810 Q666 810 698 818 Q740 835 742 900 L738 1110 Z" fill="var(--white)"/>
    <path class="windscreen" d="M466 905 L470 850 Q474 826 506 824 L680 824 Q712 826 716 850 L720 905 Q593 896 466 905 Z" fill="#151515"/>
    <path class="mirror" d="M428 885 Q428 876 436 876 L452 876 L452 924 L436 924 Q428 924 428 916 Z" fill="var(--dark)"/>
    <path class="mirror" d="M734 876 L750 876 Q758 876 758 885 L758 916 Q758 924 750 924 L734 924 Z" fill="var(--dark)"/>
    <path class="hood" d="M456 912 Q593 902 730 912 L728 1004 L458 1004 Z" fill="url(#hood-wrap)"/>
    <circle class="logo-dot" cx="593" cy="946" r="22" fill="var(--blue)"/>
    <text class="brand" x="593" y="978" font-size="15" fill="var(--blue)" text-anchor="middle">KolvanNudo</text>
    <text class="tagline" x="593" y="993" font-size="9" fill="var(--blue)" text-anchor="middle">Professional Services</text>
    <rect class="grille" x="504" y="1010" width="178" height="30" rx="3" fill="#e2e2e0"/>
    <g class="grille-slats" stroke="#9a9c9e" stroke-width="2">
      <line x1="512" y1="1020" x2="674" y2="1020"/>
      <line x1="512" y1="1030" x2="674" y2="1030"/>
    </g>
    <path class="headlight" d="M448 1008 L502 1008 L502 1030 Q470 1034 450 1030 Z" fill="#c9ccce"/>
    <rect x="448" y="1026" width="54" height="7" fill="#d97a2a"/>
    <path class="headlight" d="M684 1008 L738 1008 L736 1030 Q716 1034 684 1030 Z" fill="#c9ccce"/>
    <rect x="684" y="1026" width="54" height="7" fill="#d97a2a"/>
    <path class="bumper" d="M444 1044 L742 1044 L740 1092 Q738 1110 715 1110 L470 1110 Q448 1110 446 1092 Z" fill="var(--dark)"/>
    <rect class="plate" x="548" y="1055" width="90" height="20" rx="2" fill="#eceeee" stroke="#555" stroke-width="1"/>
  </g>
</svg>
</body>
</html>
```